Method 17 Product Guide featuring the RV-81 Vent Collector

We need a brochure on the products needed to collect a sample from a smoke stack in accordance with NRB Method 17. The feature item is the RV-81 Vent Collector (RV-81 Vent Collector) and there are several complementary items associated with the system. We need paragraph to explain each item in the system. See attached draft document. The brochure shall be a minimum of 4 pages , or 8 pages max.

Colors
33a6d7

```html
<!DOCTYPE html>
<html lang="en">
<head>
<meta charset="utf-8">
<title>Method 17 Product Guide – RV-81 Vent Collector</title>
<link href="https://fonts.googleapis.com/css2?family=Montserrat:wght@600;700;800&family=Open+Sans:wght@400;600;700&display=swap" rel="stylesheet">
<style>
:root{
  --blue:#33a6d7;
  --blue-deep:#1f7fb8;
  --navy:#1b3f73;
  --ink:#3b4450;
  --muted:#7b8794;
  --paper:#ffffff;
  --canvas:#eef1f4;
  --rule:#d5dde5;
}
*{box-sizing:border-box;margin:0;padding:0}
html,body{width:1200px;height:2400px;overflow:hidden;background:var(--canvas);font-family:"Open Sans",Arial,sans-serif;color:var(--ink)}
.board{position:relative;width:1200px;height:2400px}
.label{position:absolute;font:600 17px "Open Sans",Arial,sans-serif;color:#333}
.spread{position:absolute;left:88px;width:1052px;display:flex;box-shadow:0 6px 18px rgba(0,0,0,.18);background:var(--paper)}
.page{position:relative;width:526px;height:100%;overflow:hidden;background:var(--paper)}
.page + .page{border-left:1px solid var(--rule)}
.ph{position:absolute;background:linear-gradient(135deg,#c9d3dc,#8e9eae)}
.ph.dark{background:linear-gradient(135deg,#55606c,#2c333b)}
.ph.photo{background:linear-gradient(160deg,#8fb8d6 0%,#b8c4cc 45%,#6e7b6f 100%)}
.brand{display:flex;align-items:center;gap:8px;font:700 16px "Montserrat",Arial,sans-serif;color:var(--navy);letter-spacing:.5px}
.brand .dot{width:16px;height:16px;border-radius:50%;background:var(--blue)}
.brand.light{color:#fff}
.brand.light .dot{background:#fff}
.h{font:700 11px "Montserrat",Arial,sans-serif;color:var(--blue-deep);margin-bottom:5px}
.p{font-size:7.4px;line-height:1.5;margin-bottom:6px;text-align:justify}
.p b{color:var(--navy)}
.list{list-style:none;font-size:7.4px;line-height:1.6}
.list li{padding-left:11px;position:relative}
.list li::before{content:"";position:absolute;left:0;top:3px;width:6px;height:6px;background:var(--blue);border-radius:1px}
.bar{background:var(--blue);color:#fff;font:700 10px "Montserrat",Arial,sans-serif;letter-spacing:1px;padding:5px 10px;margin:8px 0 6px}
.ticks{list-style:none;font-size:7.2px;line-height:1.7}
.ticks li{display:flex;gap:5px;align-items:center}
.ticks svg{flex:none}
</style>
</head>
<body>
<div class="board">

  <!-- Row 1 labels -->
  <div class="label" style="left:100px;top:40px">Page 6 / Back page</div>
  <div class="label" style="left:640px;top:40px">Page 1 Front page</div>

  <section class="spread" style="top:120px;height:640px">
    <!-- Back page -->
    <article class="page back-page">
      <div style="position:absolute;left:34px;right:34px;top:30px">
        <div class="h">Introducing — XC-53 Source Sampler</div>
        <p class="p">The XC-53 Source Sampler is a compact, field-ready platform for isokinetic stack testing. It pairs precise flow control with a rugged housing so crews can move from setup to first run in minutes, even in harsh weather on elevated platforms.</p>
        <p class="p">Each console is calibrated at our facility and ships with a full report. Digital readouts track meter volume, stack temperature and velocity pressure in real time, helping operators hold isokinetic rates within the limits set by NRB Method 17.</p>
        <div class="h" style="margin-top:12px">Recommended Method 17 Sampling Kit Components</div>
        <ul class="list">
          <li>RV-81 Vent Collector metering console with umbilical</li>
          <li>In-stack filter holder with glass fiber thimble</li>
          <li>Heated probe assembly with stainless liner</li>
          <li>S-type pitot tube and thermocouple set</li>
          <li>Nozzle kit in assorted inner diameters</li>
          <li>Impinger train with ice bath case</li>
          <li>Vacuum pump and sample line fittings</li>
          <li>Calibration orifice and field check tools</li>
        </ul>
        <p class="p" style="margin-top:10px">Every component is built to work as one system. Quick connectors, matched fittings and color-coded lines reduce leak checks and keep the sampling train consistent from test to test. Our support team is ready to help you configure the right kit for your site.</p>
        <p class="p">Contact our sales engineers for pricing, lead times and training options for new field crews.</p>
      </div>
      <svg style="position:absolute;left:0;bottom:0" width="526" height="190" viewBox="0 0 526 190">
        <polygon points="0,40 526,0 526,190 0,190" fill="var(--blue)"/>
        <polygon points="0,70 526,30 526,190 0,190" fill="var(--navy)"/>
      </svg>
      <div style="position:absolute;left:34px;bottom:44px;display:flex;gap:40px;align-items:flex-end">
        <div class="brand light">Crestline Instruments</div>
        <div style="font-size:7.5px;line-height:1.6;color:#fff">
          204 Foundry Lane, Harbor Point, OR<br>
          Tel 555-014-2290<br>
          crestline-instruments.example
        </div>
      </div>
    </article>

    <!-- Front page -->
    <article class="page front-page">
      <div class="brand" style="position:absolute;left:30px;top:28px">
        <span class="dot"></span>Crestline Instruments
      </div>
      <div class="ph photo" role="img" aria-label="Technician in safety gear operating stack sampling equipment on a rooftop platform" style="left:0;top:90px;width:526px;height:360px"></div>
      <svg style="position:absolute;left:0;top:90px" width="526" height="360" viewBox="0 0 526 360">
        <polygon points="0,0 70,0 0,120" fill="var(--blue)" opacity=".85"/>
        <polygon points="0,300 526,250 526,360 0,360" fill="var(--blue)"/>
      </svg>
      <div style="position:absolute;left:0;top:450px;width:526px;height:190px;background:var(--navy)"></div>
      <svg style="position:absolute;left:0;top:410px" width="526" height="60" viewBox="0 0 526 60">
        <polygon points="0,40 526,0 526,60 0,60" fill="var(--navy)"/>
      </svg>
      <h1 style="position:absolute;right:32px;top:478px;text-align:right;color:#fff;font:800 24px/1.25 'Montserrat',Arial,sans-serif;letter-spacing:.5px">ISOKINETIC SOURCE<br>SAMPLING EQUIPMENT-</h1>
      <div style="position:absolute;right:32px;top:546px;color:var(--blue);font:800 30px 'Montserrat',Arial,sans-serif">METHOD 17</div>
    </article>
  </section>

  <!-- Row 2 labels -->
  <div class="label" style="left:100px;top:820px">Page 2</div>
  <div class="label" style="left:640px;top:820px">Page 3</div>

  <section class="spread" style="top:860px;height:740px">
    <!-- Page 2 -->
    <article class="page">
      <div style="position:absolute;left:34px;right:34px;top:30px">
        <div style="display:flex;gap:14px;margin-bottom:8px">
          <div style="width:6px;background:var(--blue)"></div>
          <div>
            <p class="p"><b>RV-81 Vent Collector</b> is designed for stable, repeatable sampling runs. The console houses the dry gas meter, orifice meter, pump controls and temperature readouts in a single weatherproof case that connects to the probe by one umbilical line.</p>
            <p class="p">The layout keeps every gauge at eye level so operators can adjust flow quickly. A bright display shows live readings, and a built-in timer logs each traverse point during the test.</p>
          </div>
        </div>
        <p class="p">The console supports both heated and unheated trains and works with standard nozzles and probes. Field crews value its light weight, sealed switches and easy leak-check valve placed on the front panel.</p>
        <p class="p">All units are bench tested before shipping and arrive with a calibration record traceable to national standards.</p>
        <div class="bar">SPECIFICATIONS</div>
        <p class="p"><b>Dry Gas Meter:</b> Positive displacement type rated for continuous sampling with a volume accuracy of one percent and a digital totalizer reading.</p>
        <p class="p"><b>Orifice Meter:</b> Inclined manometer pair for velocity and orifice pressure with ranges suited for most stack conditions.</p>
        <p class="p"><b>Pump:</b> Rotary vane vacuum pump, oil-free, rated for long duty cycles with a quiet motor and thermal overload cutout.</p>
        <p class="p"><b>Temperature Display:</b> Multi-channel digital readout for stack, probe, filter, impinger exit and meter inlet and outlet.</p>
        <p class="p"><b>Power:</b> 115 or 230 VAC, 50 or 60 Hz with a grounded cord and a resettable main breaker on the panel.</p>
        <p class="p"><b>Umbilical:</b> Lightweight jacketed bundle with vacuum line, pitot lines and thermocouple leads in lengths to suit your site.</p>
        <p class="p"><b>Case:</b> Impact resistant shell with latching lid, carry handles and stackable feet for transport.</p>
        <p class="p"><b>Weight:</b> Light enough for one person to carry to the platform with its accessory bag.</p>
      </div>
    </article>

    <!-- Page 3 -->
    <article class="page">
      <div style="position:absolute;left:30px;top:30px;width:230px">
        <div class="h">Sample Probe</div>
        <p class="p">Rigid stainless probe with a heated liner keeps sample gas above dew point from nozzle to filter.</p>
        <div class="h">Pitot Assembly</div>
        <p class="p">S-type pitot pair mounted alongside the probe to read stack velocity at each traverse point.</p>
        <div class="h">Filter Holder</div>
        <p class="p">In-stack holder sized for glass fiber thimbles, easy to open and clean between runs.</p>
      </div>
      <div class="ph" role="img" aria-label="Sample probe with pitot tube and filter holder assembly" style="left:280px;top:34px;width:210px;height:150px"></div>
      <div class="ph" role="img" aria-label="Umbilical cable coil" style="left:30px;top:250px;width:140px;height:110px"></div>
      <div class="ph" role="img" aria-label="Nozzle set in case" style="left:190px;top:250px;width:140px;height:110px"></div>
      <div class="ph" role="img" aria-label="Thermocouple leads" style="left:350px;top:250px;width:140px;height:110px"></div>
      <div style="position:absolute;left:30px;right:30px;top:380px">
        <p class="p">These accessories connect directly to the console through matched quick fittings, keeping the train tight and simple to assemble on site.</p>
        <div class="bar">RV-81 VENT COLLECTOR</div>
      </div>
      <div class="ph dark" role="img" aria-label="RV-81 Vent Collector metering console with gauges and displays" style="left:30px;top:470px;width:240px;height:230px"></div>
      <div class="ph" role="img" aria-label="Hand-held control pendant" style="left:300px;top:490px;width:190px;height:120px"></div>
      <p class="p" style="position:absolute;left:300px;top:625px;width:190px">Remote pendant lets the operator start and stop the pump from the port.</p>
    </article>
  </section>

  <!-- Row 3 labels -->
  <div class="label" style="left:100px;top:1632px">Page 4</div>
  <div class="label" style="left:640px;top:1632px">Page 5</div>

  <section class="spread" style="top:1680px;height:680px">
    <!-- Page 4 -->
    <article class="page">
      <div style="position:absolute;left:30px;right:30px;top:28px">
        <p class="p"><b>The NRB Method 17 Sampling System</b> gathers every part of the train in one matched set. Each item below plays a role in collecting a valid particulate sample from the stack.</p>
      </div>
      <div class="ph" role="img" aria-label="Glass impinger set" style="left:30px;top:84px;width:150px;height:110px"></div>
      <p class="p" style="position:absolute;left:196px;right:30px;top:90px"><b>Impinger Train:</b> Four glass impingers in an insulated ice bath case capture moisture and condensable material downstream of the filter. Ball joints and clamps keep the train sealed.</p>
      <div class="ph" role="img" aria-label="Tool kit with case" style="left:30px;top:214px;width:150px;height:110px"></div>
      <p class="p" style="position:absolute;left:196px;right:30px;top:220px"><b>Field Tool Kit:</b> Wrenches, ferrules, spare clamps and cleaning brushes packed in a foam-lined case for fast repairs at the sampling port.</p>
      <div class="ph" role="img" aria-label="Thermocouple probe set" style="left:30px;top:344px;width:150px;height:110px"></div>
      <p class="p" style="position:absolute;left:196px;right:30px;top:350px"><b>Thermocouples:</b> Type K sensors for stack, probe and impinger exit temperatures, each with a shielded lead and color-coded plug.</p>
      <div class="ph" role="img" aria-label="Calibration orifice set" style="left:30px;top:474px;width:150px;height:110px"></div>
      <p class="p" style="position:absolute;left:196px;right:30px;top:480px"><b>Calibration Orifices:</b> A set of critical orifices used to verify meter accuracy before and after each field project.</p>
      <p class="p" style="position:absolute;left:30px;right:30px;top:604px"><b>Sample Case:</b> Padded carrier holds glassware and filters securely for transport to and from the lab.</p>
    </article>

    <!-- Page 5 -->
    <article class="page">
      <div style="position:absolute;left:30px;right:30px;top:28px">
        <div class="h">Recommended Method 17 Sampling Kit Components</div>
        <div style="display:flex;gap:20px">
          <ul class="ticks" style="flex:1">
            <li><svg width="9" height="9" viewBox="0 0 10 10"><path d="M1 5l3 3 5-6" stroke="var(--blue)" stroke-width="2" fill="none"/></svg>RV-81 Vent Collector console</li>
            <li><svg width="9" height="9" viewBox="0 0 10 10"><path d="M1 5l3 3 5-6" stroke="var(--blue)" stroke-width="2" fill="none"/></svg>Heated sample probe</li>
            <li><svg width="9" height="9" viewBox="0 0 10 10"><path d="M1 5l3 3 5-6" stroke="var(--blue)" stroke-width="2" fill="none"/></svg>In-stack filter holder</li>
            <li><svg width="9" height="9" viewBox="0 0 10 10"><path d="M1 5l3 3 5-6" stroke="var(--blue)" stroke-width="2" fill="none"/></svg>S-type pitot tube</li>
          </ul>
          <ul class="ticks" style="flex:1">
            <li><svg width="9" height="9" viewBox="0 0 10 10"><path d="M1 5l3 3 5-6" stroke="var(--blue)" stroke-width="2" fill="none"/></svg>Nozzle kit</li>
            <li><svg width="9" height="9" viewBox="0 0 10 10"><path d="M1 5l3 3 5-6" stroke="var(--blue)" stroke-width="2" fill="none"/></svg>Umbilical cable</li>
            <li><svg width="9" height="9" viewBox="0 0 10 10"><path d="M1 5l3 3 5-6" stroke="var(--blue)" stroke-width="2" fill="none"/></svg>Impinger train</li>
            <li><svg width="9" height="9" viewBox="0 0 10 10"><path d="M1 5l3 3 5-6" stroke="var(--blue)" stroke-width="2" fill="none"/></svg>Calibration tools</li>
          </ul>
        </div>
      </div>
      <p class="p" style="position:absolute;left:30px;width:270px;top:130px"><b>The RV-81 Vent Collector</b> is the heart of the system. It measures sample volume and controls flow so each run stays isokinetic from start to finish, with clear displays for every reading.</p>
      <div class="ph dark" role="img" aria-label="Vacuum pump unit" style="left:320px;top:126px;width:176px;height:120px"></div>
      <p class="p" style="position:absolute;left:30px;width:270px;top:270px"><b>The Heated Probe</b> keeps gas warm on its path to the filter and is offered in several lengths to reach across large stacks and ducts.</p>
      <div class="ph" role="img" aria-label="Coiled heated sample line" style="left:320px;top:266px;width:176px;height:110px"></div>
      <p class="p" style="position:absolute;left:30px;width:270px;top:400px"><b>Nozzles</b> come in a graded set so the operator can match the inner diameter to stack velocity and hold the isokinetic ratio.</p>
      <div class="ph" role="img" aria-label="Row of sampling nozzles" style="left:320px;top:396px;width:176px;height:110px"></div>
      <p class="p" style="position:absolute;left:30px;width:270px;top:530px"><b>Clamps and Fittings</b> complete the train with leak-free joints, spare gaskets and mounting hardware for the port.</p>
      <div class="ph" role="img" aria-label="Set of clamps and fittings" style="left:320px;top:526px;width:176px;height:110px"></div>
    </article>
  </section>

</div>
</body>
</html>
```